Sale Hang Tag

Design a bright, cheerful, compelling, call to action sale tag for a lighting showroom. The tag will be used to move older or discontinued product at a really good price. Upscale, friendly, neighbor store. Size should be no larger than 4 by 6 inches.

Call

```html
<!DOCTYPE html>
<html lang="en">
<head>
<meta charset="utf-8">
<title>Sale Hang Tags</title>
<link rel="stylesheet" href="https://fonts.googleapis.com/css2?family=Libre+Baskerville:wght@400&display=swap">
<style>
  :root {
    --bg-light: #ddd6ea;
    --bg-deep: #bfaed6;
    --white: #ffffff;
    --sale-blue-bright: #1b9ad8;
    --sale-blue-deep: #1f6cb4;
    --shadow: rgba(70, 50, 100, 0.35);

    --warm-red: #e5383c;
    --warm-salmon: #ef8b7b;
    --warm-violet: #9a7dc2;
    --warm-teal: #16a7a6;
    --warm-lilac: #8e82c9;

    --cool-olive: #a9a98f;
    --cool-blue: #2c68a8;
    --cool-crimson: #c23a5c;
    --cool-orange: #ee8c5a;
    --cool-yellow: #f8e28c;
    --cool-stone: #b7ae9f;
  }
  * { margin: 0; padding: 0; box-sizing: border-box; }
  html, body { width: 1200px; height: 897px; overflow: hidden; }
  body {
    background: linear-gradient(90deg, var(--bg-light), var(--bg-deep));
    position: relative;
    font-family: "Libre Baskerville", Georgia, serif;
  }
  .hang-tag {
    position: absolute;
    top: 129px;
    width: 290px;
    height: 638px;
  }
  .hang-tag--warm { left: 220px; }
  .hang-tag--cool { left: 686px; }

  .hang-tag__loop {
    position: absolute;
    left: 110px;
    top: 0;
    width: 70px;
    height: 210px;
  }
  .hang-tag__card {
    position: absolute;
    left: 0;
    top: 204px;
    width: 290px;
    height: 434px;
    overflow: hidden;
    box-shadow: 5px 7px 8px var(--shadow);
  }
  .hang-tag__pattern {
    position: absolute;
    inset: 0;
  }
  .hang-tag--warm .hang-tag__pattern {
    background: linear-gradient(90deg,
      var(--warm-red) 0%, var(--warm-salmon) 28%, var(--warm-violet) 50%,
      var(--warm-teal) 75%, var(--warm-lilac) 100%);
  }
  .hang-tag--cool .hang-tag__pattern {
    background: linear-gradient(90deg,
      var(--cool-olive) 0%, var(--cool-blue) 22%, var(--cool-crimson) 45%,
      var(--cool-orange) 68%, var(--cool-yellow) 86%, var(--cool-stone) 100%);
  }
  .hang-tag__cartouche {
    position: absolute;
    left: 0;
    top: 0;
    width: 290px;
    height: 434px;
  }
  .hang-tag__label {
    position: absolute;
    left: 0;
    right: 0;
    top: 186px;
    text-align: center;
    font-size: 58px;
    line-height: 1;
    letter-spacing: 1px;
  }
  .hang-tag--warm .hang-tag__label { color: var(--sale-blue-bright); }
  .hang-tag--cool .hang-tag__label { color: var(--sale-blue-deep); }
</style>
</head>
<body>

  <div class="hang-tag hang-tag--warm">
    <svg class="hang-tag__loop" viewBox="0 0 70 210" aria-hidden="true">
      <path d="M6 210 V30 A29 29 0 0 1 64 30 V210" fill="none" stroke="#ffffff" stroke-width="3"/>
    </svg>
    <div class="hang-tag__card">
      <div class="hang-tag__pattern" role="img" aria-label="White ornamental scrollwork over a red, violet and teal gradient"></div>
      <svg class="hang-tag__cartouche" viewBox="0 0 290 434" aria-hidden="true">
        <path fill="#ffffff" d="M145 102 C170 120 178 140 200 150 C222 160 240 170 240 190 L268 190 L268 238 L240 238 C240 258 222 268 200 278 C178 288 170 308 145 328 C120 308 112 288 90 278 C68 268 50 258 50 238 L22 238 L22 190 L50 190 C50 170 68 160 90 150 C112 140 120 120 145 102 Z"/>
      </svg>
      <p class="hang-tag__label">SALE</p>
    </div>
  </div>

  <div class="hang-tag hang-tag--cool">
    <svg class="hang-tag__loop" viewBox="0 0 70 210" aria-hidden="true">
      <path d="M6 210 V30 A29 29 0 0 1 64 30 V210" fill="none" stroke="#ffffff" stroke-width="3"/>
    </svg>
    <div class="hang-tag__card">
      <div class="hang-tag__pattern" role="img" aria-label="White ornamental scrollwork over a blue, crimson, orange and yellow gradient"></div>
      <svg class="hang-tag__cartouche" viewBox="0 0 290 434" aria-hidden="true">
        <path fill="#ffffff" d="M145 102 C170 120 178 140 200 150 C222 160 240 170 240 190 L268 190 L268 238 L240 238 C240 258 222 268 200 278 C178 288 170 308 145 328 C120 308 112 288 90 278 C68 268 50 258 50 238 L22 238 L22 190 L50 190 C50 170 68 160 90 150 C112 140 120 120 145 102 Z"/>
      </svg>
      <p class="hang-tag__label">SALE</p>
    </div>
  </div>

</body>
</html>
```